E-commerce Website needs category banner

What we need for our category banner is a clean, predominately black design that showcases the product we are trying to sell (currently only 1), and a few subtle gradients that follow the pattern set by previous designs.

An example will be provided to showcase what we want.

It needs to say:
Outdoor Motion Detection Lighting in large, clear font similar to the example provided.
Updates

Please ensure dimensions are as follows: 980x300

Target Market(s)

Senior citizens, businesses, homeowners, families, etc

Industry/Entity Type

Product

Font styles to use
Sans Serif

Requirements
Must have
• It needs to say:
Outdoor Motion Detection Lighting in large, clear font similar to the example provided
980x300 is the required size!
Should not have
• Too much going on- clean and simple please (no crazy fonts, logos, etc)

```html
<!DOCTYPE html>
<html lang="en">
<head>
<meta charset="utf-8">
<title>Outdoor Motion Detection Lighting – Category Banner</title>
<link rel="stylesheet" href="https://fonts.googleapis.com/css2?family=Source+Sans+3:wght@700&display=swap">
<style>
  :root {
    --bg-center: #595959;
    --bg-mid: #3e3e3e;
    --bg-edge: #262626;
    --headline: #ffffff;
    --headline-shadow: rgba(0, 0, 0, 0.65);
    --product-light: #e9e9e6;
    --product-shade: #bdbdb8;
  }
  * { margin: 0; padding: 0; box-sizing: border-box; }
  html, body {
    width: 1200px;
    height: 367px;
    overflow: hidden;
    background: var(--bg-edge);
  }
  .category-banner {
    position: relative;
    width: 1200px;
    height: 367px;
    overflow: hidden;
    background:
      radial-gradient(ellipse 620px 300px at 50% 55%, var(--bg-center) 0%, var(--bg-mid) 55%, var(--bg-edge) 100%);
  }
  .banner-headline {
    position: absolute;
    left: 100px;
    top: 102px;
    font-family: "Source Sans 3", "Myriad Pro", Arial, sans-serif;
    font-weight: 700;
    font-size: 76px;
    line-height: 90px;
    letter-spacing: -1px;
    color: var(--headline);
    text-transform: uppercase;
    text-shadow: 2px 3px 4px var(--headline-shadow);
  }
  .banner-headline span { display: block; white-space: nowrap; }
  .product-shot {
    position: absolute;
    left: 851px;
    top: 24px;
    width: 234px;
    height: 331px;
    border-radius: 18px;
    background: radial-gradient(ellipse at 45% 40%, var(--product-light) 0%, var(--product-shade) 100%);
  }
</style>
</head>
<body>
  <section class="category-banner">
    <h1 class="banner-headline">
      <span>Outdoor Motion</span>
      <span>Detection Lighting</span>
    </h1>
    <div class="product-shot" role="img" aria-label="Product photo: white wireless LED motion-sensor spotlight on an adjustable wall mount"></div>
  </section>
</body>
</html>
```